Willow Crest Mind Studio

I need a brain fitness website that is on the WordPress platform. It needs to feel friendly and relaxing. We are not a physical health gym, but a brain health coaching facility. I can produce hundreds of professional photos. It can be one long page or five short pages.

Industry/Entity Type

Health And Wellness

```html
<!DOCTYPE html>
<html lang="en">
<head>
<meta charset="utf-8">
<title>Willow Crest Mind Studio</title>
<link rel="stylesheet" href="https://fonts.googleapis.com/css2?family=Lato:wght@400;700&family=Open+Sans:ital,wght@0,400;0,600;0,700;1,400&display=swap">
<style>
:root{
  --brand:#a3245c;
  --brand-dark:#8c1d4e;
  --hero:#c495ae;
  --ink:#1e1e1e;
  --body:#555;
  --muted:#888;
  --soft:#f4f4f4;
  --sky:#dcedf6;
  --white:#fff;
}
*{box-sizing:border-box;margin:0;padding:0}
html,body{width:1200px;height:3600px;overflow:hidden}
body{font-family:"Open Sans",Arial,sans-serif;color:var(--body);background:var(--white);position:relative}
section,header,footer{position:absolute;left:0;width:1200px}
h2,h3,h4{font-family:"Lato","Open Sans",sans-serif;color:var(--ink)}
.ph{display:block}

/* header */
.site-header{top:0;height:150px}
.brand{position:absolute;left:100px;top:18px;width:220px;text-align:center}
.brand-dot{width:74px;height:74px;border-radius:50%;background:#d9c7d6;margin:0 auto 8px}
.brand-name{font-family:"Lato",sans-serif;font-weight:700;font-size:20px;color:var(--brand);letter-spacing:.3px;white-space:nowrap}
.quote-btn{position:absolute;left:617px;top:26px;width:170px;height:42px;background:var(--brand);color:var(--white);font-weight:700;font-size:15px;display:flex;align-items:center;justify-content:center}
.top-divider{position:absolute;left:832px;top:22px;width:1px;height:62px;background:#ddd}
.top-contact{position:absolute;left:880px;font-size:14px;color:var(--ink);display:flex;align-items:center;gap:10px}
.top-contact svg{width:16px;height:16px;fill:var(--brand)}
.main-nav{position:absolute;left:520px;top:97px;display:flex;gap:30px;font-size:16px;color:var(--ink)}
.main-nav .active{color:var(--brand);font-weight:600}
.main-nav svg{width:17px;height:17px;margin-top:2px}

/* hero */
.hero{top:150px;height:510px;background:var(--hero);overflow:hidden}
.hero-art{position:absolute;left:700px;top:0;width:500px;height:510px;background:linear-gradient(160deg,#e9dfe6 0%,#f5f1f4 55%,#cfa9bd 100%)}
.hero-copy{position:absolute;left:100px;top:100px;color:var(--white)}
.hero-copy h1{font-family:"Lato",sans-serif;font-weight:700;font-size:52px;line-height:1.12;letter-spacing:.5px}
.hero-copy p{font-size:30px;line-height:1.4;margin-top:14px;width:560px}
.hero-btn{display:inline-block;margin-top:42px;border:2px solid var(--white);padding:9px 16px;font-size:16px}
.hero-dots{position:absolute;left:572px;top:447px;display:flex;gap:6px}
.hero-dots span{width:10px;height:10px;border-radius:50%;border:1.5px solid var(--white)}
.hero-dots span.on{background:var(--white)}

/* about */
.about{top:660px;height:505px}
.about-art{position:absolute;left:100px;top:100px;width:350px;height:250px;background:radial-gradient(circle at 55% 60%,#f0b08e 0%,#d9c2b8 35%,#fff 70%)}
.about-copy{position:absolute;left:600px;top:68px;width:490px}
.about-copy h2{font-size:30px;font-weight:700;margin-bottom:22px}
.about-copy p{font-size:14px;line-height:1.95;color:var(--ink);text-align:justify;margin-bottom:10px}
.btn{display:inline-block;background:var(--brand);color:var(--white);font-weight:700;font-size:14px;padding:10px 16px;margin-top:24px}

/* services */
.services{top:1165px;height:615px;background:var(--soft)}
.section-title{text-align:center;font-size:29px;font-weight:700}
.services .section-title{margin-top:70px}
.service-grid{position:absolute;left:100px;top:140px;width:1000px;display:grid;grid-template-columns:repeat(3,1fr);row-gap:52px;column-gap:50px}
.service-icon{width:40px;height:40px;border-radius:50%;background:var(--brand);margin-bottom:20px}
.service h3{font-family:"Open Sans",sans-serif;font-weight:400;font-size:20px;margin-bottom:12px}
.service p{font-size:13px;line-height:1.95;color:var(--muted)}

/* what we do */
.work{top:1780px;height:485px}
.work .section-title{margin-top:70px}
.work-cards{position:absolute;left:100px;top:143px;width:1000px;display:flex;justify-content:space-between}
.work-card{width:238px;height:216px;border:1px solid #ddd;border-radius:14px;overflow:hidden;box-shadow:0 2px 6px rgba(0,0,0,.08)}
.work-card .ph{height:152px}
.work-card h4{font-family:"Open Sans",sans-serif;font-weight:400;font-size:19px;text-align:center;margin-top:15px}
.view-all{position:absolute;left:0;width:1200px;top:397px;text-align:center;font-size:15px;color:var(--brand);text-decoration:underline}

/* testimonial */
.testimonial{top:2265px;height:485px;background:linear-gradient(180deg,#dfeef6,#e9f4f9)}
.testimonial .section-title{margin-top:78px;font-size:28px}
.avatar{position:absolute;left:543px;top:130px;width:114px;height:114px;border-radius:50%;border:4px solid var(--white);background:radial-gradient(circle at 50% 40%,#e8c5a6,#a86b4a)}
.quote{position:absolute;left:150px;top:272px;width:900px;text-align:center;font-size:14px;line-height:2;color:var(--ink)}
.author{position:absolute;left:0;width:1200px;top:360px;text-align:center;font-style:italic;font-size:14px;color:var(--brand);line-height:2}
.slide-arrow{position:absolute;top:238px;width:34px;height:34px;border-radius:50%;background:rgba(255,255,255,.5);display:flex;align-items:center;justify-content:center}
.slide-arrow svg{width:14px;height:14px;stroke:#9bb;fill:none;stroke-width:2.5}

/* blog */
.blog{top:2750px;height:510px}
.blog .section-title{margin-top:75px}
.blog-cards{position:absolute;left:100px;top:145px;width:1000px;display:flex;justify-content:space-between}
.blog-card{width:328px;position:relative}
.blog-card .ph{height:240px}
.blog-tag{position:absolute;left:30px;top:170px;width:268px;height:66px;background:rgba(255,255,255,.85);text-align:center;padding-top:34px;font-family:"Lato",sans-serif;font-weight:700;font-size:17px;color:var(--ink)}
.blog-meta{margin:0 30px;background:var(--white);border:1px solid #e4e4e4;border-top:0;height:36px;display:flex;align-items:center;padding-left:20px;gap:8px;font-size:12px;color:#666}
.blog-meta i{display:inline-block;width:11px;height:11px;background:var(--brand);border-radius:2px}

/* footer */
.site-footer{top:3260px;height:340px;background:var(--brand);color:var(--white)}
.footer-col{position:absolute;top:65px}
.footer-col h4{font-family:"Open Sans",sans-serif;color:var(--white);font-size:20px;font-weight:600;margin-bottom:18px}
.footer-col p{font-size:13px;line-height:1.7}
.socials{display:flex;gap:22px;margin-top:34px}
.socials span{width:18px;height:18px;border-radius:50%;background:var(--white)}
.subscribe{display:flex;margin-top:22px}
.subscribe .field{width:180px;height:36px;background:var(--white);color:#999;font-size:12px;padding:10px 12px}
.subscribe .go{width:102px;height:36px;background:#2fb6e0;color:var(--white);font-size:12px;font-weight:700;display:flex;align-items:center;justify-content:center}
.contact-list li{list-style:none;display:flex;gap:18px;font-size:13px;line-height:1.7;margin-bottom:8px}
.contact-list svg{width:14px;height:14px;fill:var(--white);flex:none;margin-top:3px}
.footer-rule{position:absolute;left:100px;top:245px;width:1000px;height:1px;background:rgba(255,255,255,.35)}
.copyright{position:absolute;left:0;width:1200px;top:278px;text-align:center;font-size:13px}
</style>
</head>
<body>

<header class="site-header">
  <div class="brand">
    <div class="brand-dot"></div>
    <div class="brand-name">Willow Crest Mind Studio</div>
  </div>
  <div class="quote-btn">Request a Quote</div>
  <div class="top-divider"></div>
  <div class="top-contact" style="top:22px">
    <svg viewBox="0 0 16 16"><path d="M1 3h14v10H1z M1 3l7 6 7-6" /></svg>hello@willowcrestmind.com
  </div>
  <div class="top-contact" style="top:60px">
    <svg viewBox="0 0 16 16"><path d="M3 1l3 3-2 2c1 2 3 4 5 5l2-2 3 3-2 3C7 15 1 9 1 3z"/></svg>Call Us : 412 - 555 - 0187
  </div>
  <nav class="main-nav">
    <span class="active">Home</span><span>About Us</span><span>Services</span><span>Training</span><span>Tips</span><span>Blog</span><span>Contact Us</span>
    <svg viewBox="0 0 16 16"><circle cx="6.5" cy="6.5" r="5" fill="none" stroke="#1e1e1e" stroke-width="2"/><path d="M10.5 10.5l4 4" stroke="#1e1e1e" stroke-width="2.2"/></svg>
  </nav>
</header>

<section class="hero">
  <div class="hero-art ph" role="img" aria-label="Illustration of a head in profile with a wrench turning a nut inside the brain"></div>
  <div class="hero-copy">
    <h1>WILLOW CREST<br>MIND STUDIO</h1>
    <p>A brain fitness facility &amp; brain health coaching facility</p>
    <span class="hero-btn">Learn More</span>
  </div>
  <div class="hero-dots"><span class="on"></span><span></span><span></span><span></span></div>
</section>

<section class="about">
  <div class="about-art ph" role="img" aria-label="Illustration of a brain lifting a heavy barbell"></div>
  <div class="about-copy">
    <h2>About Us</h2>
    <p>At vero eos et accusamus et iusto odio dignissimos ducimus qui blanditiis praesentium voluptatum deleniti atque corrupti.</p>
    <p>Et harum quidem rerum facilis est et expedita distinctio. Nam libero tempore, cum soluta nobis est eligendi optio cumque nihil impedit quo minus id quod maxime placeat facere possimus, omnis voluptas assumenda est, omnis dolor repellendus. Temporibus autem quibusdam et aut officiis debitis aut rerum necessitatibus saepe eveniet ut et voluptates repudiandae sint et molestiae non recusandae.</p>
    <span class="btn">Read More</span>
  </div>
</section>

<section class="services">
  <h2 class="section-title">Our Services</h2>
  <div class="service-grid">
    <div class="service"><div class="service-icon"></div><h3>Guidance</h3><p>Lorem ipsum dolor sit amet, consectetur elit, sed do eiusmod tempor ut labore et dolore magna adipisicing elit.</p></div>
    <div class="service"><div class="service-icon"></div><h3>Support</h3><p>Lorem ipsum dolor sit amet, consectetur elit, sed do eiusmod tempor ut labore et dolore magna adipisicing elit.</p></div>
    <div class="service"><div class="service-icon"></div><h3>Stimulation</h3><p>Lorem ipsum dolor sit amet, consectetur elit, sed do eiusmod tempor ut labore et dolore magna adipisicing elit.</p></div>
    <div class="service"><div class="service-icon"></div><h3>Effectives</h3><p>Lorem ipsum dolor sit amet, consectetur elit, sed do eiusmod tempor ut labore et dolore magna adipisicing elit.</p></div>
    <div class="service"><div class="service-icon"></div><h3>Customized</h3><p>Lorem ipsum dolor sit amet, consectetur elit, sed do eiusmod tempor ut labore et dolore magna adipisicing elit.</p></div>
    <div class="service"><div class="service-icon"></div><h3>Thrive</h3><p>Lorem ipsum dolor sit amet, consectetur elit, sed do eiusmod tempor ut labore et dolore magna adipisicing elit.</p></div>
  </div>
</section>

<section class="work">
  <h2 class="section-title">What We Do?</h2>
  <div class="work-cards">
    <div class="work-card"><div class="ph" style="height:152px;background:linear-gradient(135deg,#3a3a3a,#8a7a55)" role="img" aria-label="Photo of a glowing brain above a person on a dark backdrop"></div><h4>Human Happiness</h4></div>
    <div class="work-card"><div class="ph" style="height:152px;background:linear-gradient(135deg,#0f2a55,#4f86c6)" role="img" aria-label="Photo of a hand touching a digital training screen"></div><h4>Actual Training</h4></div>
    <div class="work-card"><div class="ph" style="height:152px;background:linear-gradient(135deg,#f2f2f2,#b9c3d6)" role="img" aria-label="Photo of a hand placing a puzzle piece"></div><h4>Voluptatum</h4></div>
    <div class="work-card"><div class="ph" style="height:152px;background:linear-gradient(135deg,#444,#9a9a9a)" role="img" aria-label="Photo of a head icon with gears on a dark background"></div><h4>Indignation</h4></div>
  </div>
  <div class="view-all">View All</div>
</section>

<section class="testimonial">
  <h2 class="section-title">Join 1000’s of People Benefiting From Willow Crest</h2>
  <div class="avatar ph" role="img" aria-label="Portrait photo of the client giving the testimonial"></div>
  <div class="slide-arrow" style="left:34px"><svg viewBox="0 0 14 14"><path d="M9 2L4 7l5 5"/></svg></div>
  <div class="slide-arrow" style="left:1132px"><svg viewBox="0 0 14 14"><path d="M5 2l5 5-5 5"/></svg></div>
  <p class="quote">“With CloudDesk Suite, maintenance employees anywhere on Redfern’s network canaccess the emails that they need to help operate the railroad; mechanics in a shop can check their manuals online, and marketing reps can download service presentations while in a customers’ office. Improved mobile productivity means keeping up with business demands.”</p>
  <div class="author">Marla Hensley, Chief Information Officer<br>Redfern Freight Lines</div>
</section>

<section class="blog">
  <h2 class="section-title">From The Blog</h2>
  <div class="blog-cards">
    <article class="blog-card">
      <div class="ph" style="height:240px;background:linear-gradient(135deg,#e8e4dc,#a89a84)" role="img" aria-label="Photo of a man thinking with gears around his head"></div>
      <div class="blog-tag">DESERUNT MOLLITIA</div>
      <div class="blog-meta"><i></i>May 15, 2017 &nbsp;| <i></i>3 Comments</div>
    </article>
    <article class="blog-card">
      <div class="ph" style="height:240px;background:linear-gradient(135deg,#0d2c5c,#6fb2ea)" role="img" aria-label="Photo of glowing brain held between two hands"></div>
      <div class="blog-tag">VOLUPTATIBUS</div>
      <div class="blog-meta"><i></i>May 16, 2017 &nbsp;| <i></i>5 Comments</div>
    </article>
    <article class="blog-card">
      <div class="ph" style="height:240px;background:linear-gradient(135deg,#c9c3c0,#6b3b3b)" role="img" aria-label="Photo of a hand holding a light bulb with a brain inside"></div>
      <div class="blog-tag">DEMORALIZED</div>
      <div class="blog-meta"><i></i>May 12, 2017 &nbsp;| <i></i>6 Comments</div>
    </article>
  </div>
</section>

<footer class="site-footer">
  <div class="footer-col" style="left:100px;width:260px">
    <h4>WILLOW CREST</h4>
    <p>Lorem ipsum dolor sit amet, consectetur adipiscing elit, sed do eiusmod tempor incididunt ut labore et dolore magna aliqua</p>
    <div class="socials"><span></span><span></span><span></span><span></span><span></span></div>
  </div>
  <div class="footer-col" style="left:440px;width:300px">
    <h4>NEWSLETTER</h4>
    <p>Subscribe our newslwtter for more informaton about mind fitness</p>
    <div class="subscribe"><div class="field">Your mail</div><div class="go">SUBSCRIBE</div></div>
  </div>
  <div class="footer-col" style="left:810px;width:300px">
    <h4>CONTACT</h4>
    <ul class="contact-list">
      <li><svg viewBox="0 0 14 14"><path d="M13 1L1 6l5 2 2 5z"/></svg>Lorem ipsum dolor sit amet, consectetur adipiscing elit</li>
      <li><svg viewBox="0 0 14 14"><path d="M1 3h12v8H1z" fill="none" stroke="#fff" stroke-width="1.4"/></svg>hello@willowcrestmind.com</li>
      <li><svg viewBox="0 0 16 16"><path d="M3 1l3 3-2 2c1 2 3 4 5 5l2-2 3 3-2 3C7 15 1 9 1 3z"/></svg>412 - 555 - 0187</li>
    </ul>
  </div>
  <div class="footer-rule"></div>
  <div class="copyright">©Copyright 2018 - Willow Crest - All Rights Reserved</div>
</footer>

</body>
</html>
```